Carrowell Business Card Re-design

Our current cards are outdated. This is our website www.carrowellinsights.example. We would like something that is "on-brand" and consistent with our social media sites. We are strategic consultants with a core competency in Marketing Research. Although, please know we are considering a brand logo redesign and potentially a new look. If we like your work here we will invite you to participate when we get to that project. Thank you very much. Harriet
Here are our social sites: https://twitter.com/Carrowell?lang=en
https://plus.google.com/+Carrowellinsights
https://www.linkedin.com/company/5094827/
https://www.facebook.com/CarrowellInc/
Business

```html
<!DOCTYPE html>
<html lang="en">
<head>
<meta charset="utf-8">
<title>Carrowell Business Card</title>
<link href="https://fonts.googleapis.com/css2?family=Arimo:wght@400;700&display=swap" rel="stylesheet">
<style>
  :root {
    --brand-green: #7fa33e;
    --brand-blue: #3a6796;
    --card-white: #ffffff;
    --page-bg: #ffffff;
    --icon-ink: #111111;
  }
  * { margin: 0; padding: 0; box-sizing: border-box; }
  html, body {
    width: 1200px;
    height: 1200px;
    overflow: hidden;
    background: var(--page-bg);
    font-family: "Arimo", Arial, sans-serif;
  }
  .canvas { position: relative; width: 1200px; height: 1200px; }
  .card {
    position: absolute;
    left: 186px;
    width: 838px;
    background: var(--card-white);
    box-shadow: 0 10px 28px rgba(0, 0, 0, 0.12);
    overflow: hidden;
  }
  .card--front { top: 62px; height: 478px; }
  .card--back { top: 636px; height: 476px; }
  .card svg { display: block; width: 100%; height: 100%; }
  .fill-green { fill: var(--brand-green); }
  .fill-blue { fill: var(--brand-blue); }
  .brand-name { font-family: "Arimo", Arial, sans-serif; font-weight: 700; }
  .brand-name--diagonal { fill: var(--card-white); font-size: 66px; }
  .brand-name--hero { fill: var(--brand-green); font-size: 112px; }
  .person-first { fill: var(--brand-green); font-weight: 700; font-size: 32px; }
  .person-last { fill: var(--brand-blue); font-weight: 700; font-size: 32px; }
  .person-title { fill: var(--brand-green); font-size: 21px; }
  .contact-line { fill: var(--brand-green); font-size: 18px; }
  .site-url { fill: var(--brand-green); font-size: 22px; }
  .rule { stroke: var(--brand-green); stroke-width: 2; }
  .icon-line { stroke: var(--icon-ink); fill: none; stroke-width: 1.6; }
  .icon-solid { fill: var(--icon-ink); }
</style>
</head>
<body>
<main class="canvas">

  <section class="card card--front" aria-label="Business card front">
    <svg viewBox="0 0 698 398" xmlns="http://www.w3.org/2000/svg">
      <polygon class="fill-blue" points="430,0 698,0 698,133"/>
      <polygon class="fill-blue" points="197,191 237,398 0,398"/>
      <polygon class="fill-green" points="0,0 378,0 0,398"/>

      <text class="brand-name brand-name--diagonal" x="160" y="190" text-anchor="middle"
            transform="rotate(-44 160 168)">carrowell</text>

      <text x="320" y="173"><tspan class="person-first">Harriet</tspan><tspan class="person-last" dx="8">Pemberton</tspan></text>
      <line class="rule" x1="318" y1="184" x2="669" y2="184"/>
      <text class="person-title" x="320" y="213">Marketing Researcher</text>

      <g class="contact-icon contact-icon--phone">
        <rect class="icon-solid" x="322" y="252" width="16" height="29" rx="3"/>
        <rect fill="#fff" x="325" y="256" width="10" height="19"/>
      </g>
      <text class="contact-line" x="365" y="275">+1-555-014-229</text>

      <g class="contact-icon contact-icon--mail">
        <rect class="icon-solid" x="316" y="294" width="32" height="20"/>
        <polyline points="317,295 332,307 347,295" fill="none" stroke="#fff" stroke-width="2"/>
      </g>
      <text class="contact-line" x="365" y="309">info@carrowellinsights.example</text>

      <g class="contact-icon contact-icon--globe">
        <circle class="icon-line" cx="332" cy="338" r="15"/>
        <ellipse class="icon-line" cx="332" cy="338" rx="6" ry="15"/>
        <line class="icon-line" x1="317" y1="338" x2="347" y2="338"/>
        <line class="icon-line" x1="320" y1="330" x2="344" y2="330"/>
        <line class="icon-line" x1="320" y1="346" x2="344" y2="346"/>
        <line class="icon-line" x1="332" y1="323" x2="332" y2="353"/>
      </g>
      <text class="contact-line" x="365" y="344">www.carrowellinsights.example</text>
    </svg>
  </section>

  <section class="card card--back" aria-label="Business card back">
    <svg viewBox="0 0 698 397" xmlns="http://www.w3.org/2000/svg">
      <polygon class="fill-blue" points="0,0 300,0 0,125"/>
      <polygon class="fill-blue" points="698,270 698,397 435,397"/>

      <text class="brand-name brand-name--hero" x="349" y="220" text-anchor="middle">carrowell</text>
      <text class="site-url" x="52" y="248">www.carrowellinsights.example</text>
    </svg>
  </section>

</main>
</body>
</html>
```